Style Template created - Report Accounting and Advisory industry

We need a style template created to set out a report for advice. The report follows <br/><br/>- Cover Page - ( we would need to print to a letter head )<br/>- General Disclaimer<br/>- Space to add Excel Reports in to the document- Maybe inserted Pdf's later<br/>- Action Plan dot points under headings<br/>- List of Strategies to be adopted<br/><br/>Attached is a quick example word doc that needs Custom Style Templates made so that we can quickly format items added. Also the ugly PDF that we currently produce for clients <br/><br/>Red - is our preferred Colour<br/><br/>

Target Market(s)

Accounting / Business / Professionals

Industry/Entity Type

Accounting

Colors
ec1f27

Requirements
Nice to have
• Simple Clean design. Not to busy. Easy to modify the "wording text" in design
Should not have
• Too busy or too much color

```html
<!DOCTYPE html>
<html lang="en">
<head>
<meta charset="utf-8">
<title>Harlow Vance – Report Style Template</title>
<link href="https://fonts.googleapis.com/css2?family=Open+Sans:ital,wght@0,400;0,600;0,700;1,400&display=swap" rel="stylesheet">
<style>
:root{
  --backdrop:#bdbdbd;
  --paper:#ffffff;
  --brand-red:#c4161c;
  --ink:#1c1c1c;
  --muted:#555;
  --rule:#555;
  --band:#d9d9d9;
  --band-dark:#bcbcbc;
  --panel:#f1f1f1;
}
*{margin:0;padding:0;box-sizing:border-box}
html,body{width:1200px;height:1200px;overflow:hidden}
body{background:var(--backdrop);font-family:'Open Sans',Arial,sans-serif;color:var(--ink);position:relative}
.page{position:absolute;width:314px;height:443px;background:var(--paper);box-shadow:0 8px 10px rgba(0,0,0,.28);overflow:hidden}
.p1{left:70px;top:149px}.p2{left:447px;top:149px}.p3{left:824px;top:149px}
.p4{left:70px;top:661px}.p5{left:447px;top:661px}.p6{left:824px;top:661px}
.abs{position:absolute}
.mark{position:absolute;border-radius:50%;background:var(--brand-red)}
.run-head{position:absolute;top:21px;font-size:3px;font-weight:700;color:var(--ink);white-space:nowrap}
.run-rule{position:absolute;top:26px;height:1px;background:var(--rule)}
.folio{position:absolute;top:409px;background:#c8c8c8;font-size:4.6px;padding:1.5px 4px;color:#333}

/* cover */
.cover-top{left:0;top:0;width:100%;height:11px;background:#ececec}
.brand{position:absolute;font-weight:600;color:var(--brand-red);letter-spacing:.3px;white-space:nowrap}
.brand-sub{position:absolute;font-size:4px;color:var(--muted);letter-spacing:.3px}
.cover-rule{left:17px;top:49px;width:229px;height:1.3px;background:var(--brand-red)}
.client-name{left:34px;top:295px;font-size:7.5px;font-weight:700}
.client-rule{left:34px;top:305px;width:246px;height:.8px;background:#777}
.cover-title{left:34px;top:310px;font-size:6.4px;font-weight:600;color:#333}
.cover-date{left:34px;top:320px;font-size:6.4px;color:#444}
.cover-foot{left:0;top:411px;width:100%;height:32px;background:var(--band);font-size:3.2px;font-weight:700;text-align:center;padding-top:8px;line-height:5px}

/* disclaimer */
.side-bar{left:41px;top:69px;width:2px;height:280px;background:#aaa}
.disclaimer{left:61px;top:84px;width:206px;font-size:4.6px;line-height:7.6px}
.disclaimer h1{font-size:8.2px;font-weight:700;margin-bottom:3px;line-height:11px}
.disclaimer p{margin-bottom:7.6px}
.disclaimer h2{font-size:4.8px;font-weight:700;line-height:7.6px}
.sign{font-weight:700;font-size:4.8px;line-height:6.6px;margin-top:20px}

.excel-note{left:28px;top:39px;font-size:4.8px;font-style:italic}

/* action plan */
.action{position:absolute;left:28px;width:258px}
.action h2{font-size:4.6px;font-weight:700;border-bottom:1px solid var(--rule);padding-bottom:1px}
.action ul{margin:5px 0 0 38px;font-size:4.6px;font-style:italic;line-height:8px}

/* strategies */
.strat-panel{left:31px;top:39px;width:254px;height:47px;background:var(--panel);padding:4px 4px}
.strat-panel h1{font-size:9.4px;font-weight:700;line-height:11px;letter-spacing:-.2px}
.strat-panel .lead{font-size:4px;color:#333;margin-top:1px}
.strat-panel h3{font-size:6.5px;font-weight:400;margin-top:8px;line-height:7px}
.strat-panel .kicker{font-size:3.6px}
.strategy{position:absolute;left:34px;width:252px;font-size:3.5px;line-height:6.3px;color:#222}
.strategy h2{font-size:4.8px;font-weight:700;border-bottom:1px solid var(--rule);line-height:6.5px;margin-bottom:4px;color:var(--ink)}
.strategy ul{margin-left:14px}
.strategy .dash{list-style:"–  "}

.back-band{left:0;top:412px;width:100%;height:31px;background:var(--band-dark)}
</style>
</head>
<body>

<section class="page p1" aria-label="Cover page">
  <div class="abs cover-top"></div>
  <div class="brand" style="left:20px;top:19px;font-size:14px">HARLOW VANCE</div>
  <div class="brand-sub" style="left:21px;top:37px">CHARTERED ACCOUNTANTS</div>
  <div class="abs cover-rule"></div>
  <div class="mark" style="left:253px;top:15px;width:44px;height:44px"></div>
  <div class="abs client-name">CLIENT NAME</div>
  <div class="abs client-rule"></div>
  <div class="abs cover-title">TAXATION ESTIMATE FOR THE PERIOD ENDED</div>
  <div class="abs cover-date">30 JUNE 2019</div>
  <div class="abs cover-foot">Ferndale Pty Ltd ACN 200 517 946 42 Elmstead Road, Riverside, WA 6100 PO Box 2290, Harbour Point, WA 6100<br>Tel: 08 5550 1420 Fax: 08 5550 1421 Email: office@harlowvance.example Director Daniel Harlow CA</div>
</section>

<section class="page p2" aria-label="Disclaimer page">
  <div class="mark" style="left:36px;top:17px;width:20px;height:20px"></div>
  <div class="run-rule" style="left:62px;width:223px"></div>
  <div class="run-head" style="right:29px">2019 TAX PLANNING | Brightwell Equipment Hire Pty Ltd</div>
  <div class="abs side-bar"></div>
  <div class="abs disclaimer">
    <h1>DISCLAIMER</h1>
    <p>The taxation estimate has been prepared on the basis of information provided by the client. The report is intended for internal tax planning purposes and represents a "What if scenario". It does not necessarily represent real or intended transactions.</p>
    <p>HarlowVance have not performed any tests to verify or validate any of the information provided by the client and accordingly express no assurance as to the outcome indicated.</p>
    <p>To the extent permitted by law we do not accept liability for any loss or damage which any person, other than the client may suffer arising from any negligence on our part. No person should rely on the Taxation estimate without having a full review or audit conducted on the data.</p>
    <h2>Superannuation</h2>
    <p>Provision of Advice is guided by legislative requirements to be provided in a Statement of Advice. Any and all comments regarding Superannuation are not to be taken as advice rather than statement of factual information about the situation. The statement is not a recommendation to take any action unless that action is required by law. The clients personal situation has not been considered in providing the information. Any action to be taken in relation to the information provided, should take into account the clients personal situation and consideration must be given as to whether action will be appropriate for the clients' objectives and needs. Specific Contribution amounts and SMSF product advice can only be provided under a Statement of Advice by a AFSL Holder.</p>
    <div class="sign">Harlow Vance<br>Chartered Accountants</div>
  </div>
  <div class="folio" style="left:24px">Page | 2</div>
</section>

<section class="page p3" aria-label="Spreadsheet insert page">
  <div class="run-head" style="left:34px">2019 TAX PLANNING | Brightwell Equipment Hire Pty Ltd</div>
  <div class="run-rule" style="left:32px;width:225px"></div>
  <div class="mark" style="left:264px;top:17px;width:20px;height:20px"></div>
  <div class="abs excel-note">Excel sheet</div>
  <div class="folio" style="left:260px">Page | 3</div>
</section>

<section class="page p4" aria-label="Action plan page">
  <div class="mark" style="left:36px;top:17px;width:20px;height:20px"></div>
  <div class="run-rule" style="left:62px;width:223px"></div>
  <div class="run-head" style="right:29px">2019 TAX PLANNING | Brightwell Equipment Hire Pty Ltd</div>
  <div class="action" style="top:51px">
    <h2>Action Items to do now</h2>
    <ul><li>Lorem ipsum</li><li>Lorem ipsum</li><li>Lorem ipsum</li><li>Lorem ipsum</li><li>Lorem ipsum</li><li>Lorem ipsum</li></ul>
  </div>
  <div class="action" style="top:147px"><h2>Action items to see others About</h2></div>
  <div class="action" style="top:242px"><h2>Action items for after year end</h2></div>
  <div class="folio" style="left:24px">Page | 4</div>
</section>

<section class="page p5" aria-label="Tax planning strategies page">
  <div class="run-head" style="left:34px">2019 TAX PLANNING | Brightwell Equipment Hire Pty Ltd</div>
  <div class="run-rule" style="left:32px;width:225px"></div>
  <div class="mark" style="left:264px;top:17px;width:20px;height:20px"></div>
  <div class="abs strat-panel">
    <h1>TAX PLANNING STRATEGIES</h1>
    <div class="lead">A more detailed list of potential tax planning strategies is as follows:</div>
    <h3>MAIN TAX PLANNING STRATEGIES</h3>
    <div class="kicker">STRATEGY</div>
  </div>
  <div class="strategy" style="top:91px">
    <h2>Bring Forward Expenses</h2>
    If possible, you should incur any business use expenses prior to 30 June. This way that expense will be included in the current tax year rather than NEXT tax year, reducing your tax payable in this financial year.<br><br style="line-height:3px">Examples include: consumables, repairs, computer and office supplies.
  </div>
  <div class="strategy" style="top:145px">
    <h2>Defer Income</h2>
    If possible, you should defer issuing invoices in the last week or two until after 30 June 2019. This way that income will be included in the 2020 tax year rather than the 2019 tax year, deferring tax on the income for a year. Cash basis taxpayers should defer receipt of payment if possible.
  </div>
  <div class="strategy" style="top:193px">
    <h2>Accounts Receivable</h2>
    Under the small business tax concessions, the financial statements can be prepared on a cash basis so amounts receivable can be removed from the financial statements for tax purposes
  </div>
  <div class="strategy" style="top:234px">
    <h2>Accounts Payable</h2>
    Under the small business tax concessions, the financial statements can be prepared on a cash basis so amounts payable can be removed from the financial statements for tax purposes
  </div>
  <div class="strategy" style="top:275px">
    <h2>Depreciation From Purchased Assets that Cost more than $30,000</h2>
    A small business entity that purchases depreciating assets that cost more than:
    <ul class="dash" style="margin-left:18px"><li>$30,000 from 3 April 2019 – 30 June 2019</li><li>$25,000 from 29 January 2019 – 2 April 2019</li><li>$20,000 from 1 July 2018 – 28 January 2019</li></ul>
    Will receive the following tax deductions from pooling the asset(s) in a small business asset pool:
    <ul style="margin-left:18px"><li>A 15% deduction in the 2019 tax year, regardless of when you purchased the asset during the year; and</li><li>A 30% deduction each year after the first year.</li></ul>
  </div>
  <div class="strategy" style="top:368px">
    <h2>Bucket Company</h2>
    If your business is trading through a trust and you have incurred higher than normal profits or the profits earned in your business are taxed at the highest marginal tax rate then a further tax planning strategy to consider is to set up a bucket company.
  </div>
  <div class="folio" style="left:260px">Page | 5</div>
</section>

<section class="page p6" aria-label="Back cover">
  <div class="mark" style="left:128px;top:271px;width:68px;height:68px"></div>
  <div class="brand" style="left:93px;top:353px;font-size:13.5px">HARLOW VANCE</div>
  <div class="brand-sub" style="left:94px;top:370px">CHARTERED ACCOUNTANTS</div>
  <div class="abs back-band"></div>
</section>

</body>
</html>
```